New labels for new line of supplements

I'm starting a new line of supplements and I need a label created for the first supplement - Glyco Steady Aid.
The supplement line is by Corvane Nutrition. What I'm really looking for is label that can be used again for the next supplement and consumers would recognize the label layout as a Corvane Nutrition product. I've attached an example from Pelminth Nutrition to have a look at. I've also attached my "Corvane Skin Care" logo that needs to be turned into Corvane Nutrition. Just change Skin Care to Nutrition.
Target Market(s)
Trelvix consumers
Colors
Designer to choose colors to be used in the design.
Requirements
Must have
- Instantly recognizable as my brand

```html
<!DOCTYPE html>
<html lang="en">
<head>
<meta charset="utf-8">
<title>Corvane Nutrition – Glyco Steady Aid Label</title>
<link href="https://fonts.googleapis.com/css2?family=Varela+Round&family=Roboto+Condensed:wght@500;700&display=swap" rel="stylesheet">
<style>
  :root {
    --backdrop: #e4e4e4;
    --label-white: #ffffff;
    --brand-blue: #2c4f8f;
    --title-gold: #f0bd1a;
    --claim-red: #7d1c12;
    --band-orange: #f2a31b;
    --band-yellow: #f6c22e;
    --pill-brown: #6a2e1f;
    --pill-text: #ffffff;
    --cell-red: #c8102e;
    --cell-dark: #8e0a1f;
  }
  * { margin: 0; padding: 0; box-sizing: border-box; }
  html, body {
    width: 1200px;
    height: 800px;
    overflow: hidden;
    background: var(--backdrop);
  }
  .label {
    position: absolute;
    left: 320px;
    top: 52px;
    width: 570px;
    height: 696px;
    background: var(--label-white);
    overflow: hidden;
    box-shadow: 0 6px 24px rgba(0,0,0,0.08);
  }
  .brand {
    position: absolute;
    left: 31px;
    top: 90px;
    color: var(--brand-blue);
    font-family: "Varela Round", sans-serif;
    font-weight: 400;
  }
  .brand-name {
    display: block;
    font-size: 32px;
    letter-spacing: 1px;
    line-height: 1;
  }
  .brand-line {
    display: block;
    font-size: 10px;
    letter-spacing: 3px;
    margin-top: 5px;
  }
  .product-title {
    position: absolute;
    left: 31px;
    top: 194px;
    font-family: "Varela Round", sans-serif;
    font-weight: 400;
    font-size: 58px;
    line-height: 62px;
    color: var(--title-gold);
    letter-spacing: 1px;
  }
  .claims {
    position: absolute;
    left: 31px;
    top: 388px;
    list-style: none;
    font-family: "Roboto Condensed", sans-serif;
    font-weight: 500;
    font-size: 14px;
    line-height: 18px;
    color: var(--claim-red);
    text-transform: uppercase;
  }
  .claims li::before { content: "• "; }
  .band {
    position: absolute;
    left: 0;
    top: 447px;
    width: 100%;
    height: 249px;
    background: linear-gradient(160deg, var(--band-yellow) 0%, var(--band-orange) 70%);
  }
  .supplement-tag {
    position: absolute;
    left: 46px;
    top: 468px;
    width: 163px;
    height: 28px;
    border-radius: 14px;
    background: var(--pill-brown);
    color: var(--pill-text);
    font-family: "Roboto Condensed", sans-serif;
    font-weight: 700;
    font-size: 13px;
    line-height: 28px;
    text-align: center;
  }
  .count {
    position: absolute;
    left: 56px;
    top: 508px;
    font-family: "Roboto Condensed", sans-serif;
    font-weight: 700;
    font-size: 12px;
    color: var(--pill-brown);
  }
  .cells-art {
    position: absolute;
    left: 300px;
    top: 160px;
    width: 270px;
    height: 536px;
  }
</style>
</head>
<body>
  <main class="label">
    <div class="brand">
      <span class="brand-name">CORVANE</span>
      <span class="brand-line">NUTRITION</span>
    </div>

    <h1 class="product-title">GLYCO<br>STEADY<br>AID</h1>

    <ul class="claims">
      <li>Supports healthy blood sugar*</li>
      <li>Immune function support*</li>
      <li>Plus much more!*</li>
    </ul>

    <div class="band"></div>
    <div class="supplement-tag">Dietary Supplement</div>
    <div class="count">60 Capsules</div>

    <svg class="cells-art" viewBox="0 0 270 536" role="img" aria-label="Illustration of floating red blood cells">
      <defs>
        <radialGradient id="cellGlow" cx="50%" cy="50%" r="55%">
          <stop offset="0%" stop-color="#c8102e" stop-opacity="0.85"/>
          <stop offset="60%" stop-color="#8e0a1f" stop-opacity="0.45"/>
          <stop offset="100%" stop-color="#8e0a1f" stop-opacity="0"/>
        </radialGradient>
      </defs>
      <rect x="0" y="0" width="270" height="536" fill="url(#cellGlow)"/>
    </svg>
  </main>
</body>
</html>
```